We require a Squarespace web design for Ashfern Cannabis Website.
We are an urban community retail cannabis store. We have turn tables set up playing old hip hop/house music to create a lounge vibe. The store is very urban, dark and sexy. We have a couple of concepts that we like. One is a dark stone background and smoke rising up. Such as the link here. https://dev.lumo.vantrell.exampleweb.com/products/
The other is using the black and white map of our community.
We would like to have any concept include the logo on the turntable with the logo spinning like a record and the words ASHFERN CANNABIS also spinning around it (such as in the attached giff.)
We tend to gravitate toward black and white and gold for the colours.
1847 Harwick Boulevard West,
Scarborough, ON K4R 7P3
(416) 384-LEAF
Hours of Operation
Open Daily 10:00 - 10:00

```html
<!DOCTYPE html>
<html lang="en">
<head>
<meta charset="utf-8">
<title>Ashfern Cannabis</title>
<link rel="stylesheet" href="https://fonts.googleapis.com/css2?family=IM+Fell+English+SC&family=Playfair+Display:wght@400&family=Josefin+Sans:wght@600&display=swap">
<style>
:root{
  --black:#0b0b0b;
  --charcoal:#1c1c1c;
  --gold:#d9bd6e;
  --gold-btn:#e1c77f;
  --ink:#1a1a1a;
  --grey-section:#e6e6e6;
  --white:#ffffff;
}
*{margin:0;padding:0;box-sizing:border-box}
html,body{width:1200px;height:4573px;overflow:hidden}
body{position:relative;background:var(--white);font-family:"Playfair Display",Georgia,serif;color:var(--ink)}
.abs{position:absolute}
.display{font-family:"IM Fell English SC",Georgia,serif;letter-spacing:6px;text-align:center;font-weight:400}
.btn{position:absolute;background:var(--gold-btn);color:#3a2f14;font-size:19px;display:flex;align-items:center;justify-content:center;text-decoration:none}
.brand-mark{border:3px solid var(--gold);border-radius:50%}
.brand-name{font-family:"Josefin Sans",Arial,sans-serif;font-weight:600;color:var(--gold);letter-spacing:8px;line-height:1.3}

/* header + hero */
.hero{left:0;top:0;width:1200px;height:834px;
  background:
    radial-gradient(ellipse 420px 120px at 700px 190px,rgba(150,150,150,.35),transparent 70%),
    radial-gradient(ellipse 380px 140px at 250px 330px,rgba(140,140,140,.3),transparent 70%),
    radial-gradient(ellipse 460px 150px at 950px 420px,rgba(170,170,170,.35),transparent 70%),
    radial-gradient(ellipse 520px 160px at 420px 520px,rgba(210,210,210,.45),transparent 70%),
    radial-gradient(ellipse 700px 220px at 600px 700px,rgba(255,255,255,.9),transparent 75%),
    linear-gradient(180deg,#050505 0%,#161616 30%,#4a4a4a 55%,#c8c8c8 78%,#fff 100%)}
.header-mark{left:50px;top:27px;width:106px;height:106px}
.header-name{left:178px;top:52px;font-size:24px;width:260px}
.nav{top:66px;font-size:21px;color:var(--white);text-decoration:none}
.hero-faint{left:230px;top:280px;width:740px;font-size:66px;color:rgba(217,189,110,.18);letter-spacing:18px;text-align:center}

/* products */
.section-title{left:0;width:1200px;font-size:54px;color:var(--black)}
.product-photo{top:998px;width:274px;height:367px;border:2px solid #3a3a3a;
  background:
    linear-gradient(180deg,transparent 72%,#0d0d0d 72%),
    radial-gradient(ellipse 70px 110px at 50% 45%,rgba(210,215,200,.55),rgba(80,95,60,.35) 60%,transparent 100%),
    linear-gradient(180deg,#2c2c2c 0%,#1a1a1a 100%)}
.product-name{top:1396px;width:274px;text-align:center;font-size:27px}

/* banner */
.banner-photo{left:0;top:1621px;width:1200px;height:564px;
  background:
    radial-gradient(ellipse 260px 220px at 850px 180px,rgba(140,150,90,.45),transparent 70%),
    radial-gradient(ellipse 300px 200px at 200px 380px,rgba(60,80,45,.5),transparent 70%),
    linear-gradient(90deg,#0f160d 0%,#22301c 45%,#3e4d2e 70%,#1c2616 100%)}
.banner-block{left:438px;top:1947px;width:332px;height:238px;background:var(--charcoal)}
.banner-mark{left:437px;top:1716px;width:334px;height:334px;border:6px solid var(--gold)}

/* what we do */
.what{left:0;top:2185px;width:1200px;height:900px;
  background:
    radial-gradient(ellipse 400px 180px at 200px 150px,#c4c4c4,transparent 70%),
    radial-gradient(ellipse 420px 200px at 1000px 120px,#cdcdcd,transparent 70%),
    radial-gradient(ellipse 300px 160px at 100px 520px,#d2d2d2,transparent 70%),
    var(--grey-section)}
.what-photo{top:2412px;width:479px;height:322px}
.what-heading{top:2770px;width:479px;text-align:center;font-size:27px;font-weight:400}
.what-body{top:2822px;width:479px;text-align:center;font-size:16px;line-height:24px;color:#333}

/* signup */
.signup{left:0;top:3085px;width:1200px;height:431px;background:linear-gradient(90deg,#140609 0%,#1a0d10 40%,#2c3b22 65%,#3e5530 100%)}
.signup-input{left:261px;top:3321px;width:513px;height:60px;background:var(--white);font-size:29px;padding:10px 14px;color:#111}

/* about */
.about-photo{left:114px;top:3699px;width:472px;height:472px;border-radius:50%;background:linear-gradient(135deg,#1e2a1a 0%,#3b4a2e 45%,#c9825d 75%,#f2d6c2 100%)}
.about-body{left:643px;top:3805px;width:420px;font-size:15.5px;line-height:24px;color:#222}

/* footer */
.footer{left:0;top:4292px;width:1200px;height:281px;background:var(--charcoal)}
.footer-text{font-size:17px;line-height:22px;color:var(--white)}
.footer-phone{color:var(--gold)}
.footer-mark{left:410px;top:4363px;width:106px;height:106px}
.footer-name{left:540px;top:4385px;font-size:24px;width:260px}
.social-list{left:850px;top:4447px;display:flex;gap:22px;list-style:none}
.social{font-size:15px;color:var(--white);white-space:nowrap}
</style>
</head>
<body>

<!-- hero -->
<section class="abs hero" role="img" aria-label="Smoke rising over a dark stone background"></section>
<div class="abs brand-mark header-mark"></div>
<div class="abs brand-name header-name">ASHFERN<br><span style="font-size:16px;letter-spacing:6px">CANNABIS</span></div>
<nav>
  <a class="abs nav" style="left:547px">Shop</a>
  <a class="abs nav" style="left:634px">Our Story</a>
  <a class="abs nav" style="left:758px">Ashfern</a>
  <a class="abs nav" style="left:886px">Contact</a>
</nav>
<svg class="abs" style="left:1006px;top:62px" width="44" height="40" viewBox="0 0 44 40" aria-label="Cart">
  <path d="M2 4h7l5 22h22l5-16H12" fill="none" stroke="var(--gold)" stroke-width="3" stroke-linejoin="round"/>
  <circle cx="17" cy="34" r="3" fill="var(--gold)"/><circle cx="33" cy="34" r="3" fill="var(--gold)"/>
</svg>
<div class="abs brand-name hero-faint">ASHFERN</div>
<svg class="abs" style="left:548px;top:303px" width="104" height="104" viewBox="0 0 104 104" aria-label="Play video">
  <circle cx="52" cy="52" r="48" fill="none" stroke="#fff" stroke-width="4"/>
  <path d="M42 32v40l30-20z" fill="#fff"/>
</svg>

<!-- products -->
<h2 class="abs display section-title" style="top:868px">OUR PRODUCTS</h2>
<div class="abs product-photo" style="left:142px" role="img" aria-label="Glass jar of cannabis flower on a black stand"></div>
<div class="abs product-photo" style="left:463px" role="img" aria-label="Glass jar of cannabis flower on a black stand"></div>
<div class="abs product-photo" style="left:785px" role="img" aria-label="Glass jar of cannabis flower on a black stand"></div>
<p class="abs product-name" style="left:142px">Product Name</p>
<p class="abs product-name" style="left:463px">Product Name</p>
<p class="abs product-name" style="left:785px">Product Name</p>
<a class="btn" style="left:213px;top:1450px;width:131px;height:52px">Shop Now</a>
<a class="btn" style="left:535px;top:1450px;width:131px;height:52px">Shop Now</a>
<a class="btn" style="left:855px;top:1450px;width:131px;height:52px">Shop Now</a>

<!-- banner -->
<section class="abs banner-photo" role="img" aria-label="Close-up of cannabis plants in bloom"></section>
<div class="abs banner-block"></div>
<div class="abs brand-mark banner-mark"></div>
<div class="abs brand-name" style="left:438px;top:1860px;width:332px;text-align:center;font-size:30px">ASHFERN</div>

<!-- what we do -->
<section class="abs what" role="img" aria-label="Soft white smoke on light grey"></section>
<h2 class="abs display section-title" style="top:2274px">WHAT WE DO</h2>
<div class="abs what-photo" style="left:94px;background:radial-gradient(ellipse 90px 140px at 50% 55%,#5d6e3c,#2a361c 60%,#050505 100%)" role="img" aria-label="Green cannabis bud on black"></div>
<div class="abs what-photo" style="left:627px;background:radial-gradient(ellipse 180px 130px at 50% 55%,#6c5288,#34243f 60%,#050505 100%)" role="img" aria-label="Purple cannabis plant on black"></div>
<h3 class="abs what-heading" style="left:94px">Is It Flowers You’re After?</h3>
<h3 class="abs what-heading" style="left:627px">Searching for Cannabis?</h3>
<p class="abs what-body" style="left:94px">Lorem ipsum dolor sit amet, consectetur adipiscing<br>usmod tempor incididunt ut labore et.</p>
<p class="abs what-body" style="left:627px">Lorem ipsum dolor sit amet, consectetur adipiscing<br>usmod tempor incididunt ut labore et.</p>
<a class="btn" style="left:266px;top:2897px;width:137px;height:51px">Read More</a>
<a class="btn" style="left:797px;top:2897px;width:138px;height:51px">Read More</a>

<!-- signup -->
<section class="abs signup" role="img" aria-label="Cannabis leaves fading into dark plum"></section>
<h2 class="abs display section-title" style="top:3202px;color:#fff">THEY GROW UP SO FAST.</h2>
<div class="abs signup-input">Email:</div>
<a class="btn" style="left:786px;top:3321px;width:151px;height:60px;font-size:29px">Sign up</a>

<!-- about -->
<div class="abs about-photo" role="img" aria-label="Hand holding a joint, framed in a circle"></div>
<h2 class="abs display" style="left:643px;top:3700px;font-size:54px;color:var(--black);text-align:left">ABOUT US</h2>
<p class="abs about-body">Lorem ipsum dolor sit amet, consectetur adipiscing elit, sed do eiusmod tempor incididunt ut labore et dolore magna aliqua. Quis ipsum suspendisse ultrices gravida. Risus commodo viverra maecenas accumsan lacus vel facilisis. Lorem ipsum dolor sit amet, consectetur adipiscing elit, sed do eiusmod tempor incididunt ut labore et dolore magna aliqua. Quis ipsum suspendisse ultrices gravida. Risus commodo viverra maecenas accumsan lacus vel facilisis.</p>
<a class="btn" style="left:641px;top:4045px;width:137px;height:51px">Read More</a>

<!-- footer -->
<footer class="abs footer"></footer>
<p class="abs footer-text" style="left:149px;top:4375px">Location<br>1847 Harwick Boulevard West,<br>Scarborough, ON K4R 7P3</p>
<p class="abs footer-text footer-phone" style="left:149px;top:4458px">(416) 384-LEAF</p>
<div class="abs brand-mark footer-mark"></div>
<div class="abs brand-name footer-name">ASHFERN<br><span style="font-size:16px;letter-spacing:6px">CANNABIS</span></div>
<p class="abs footer-text" style="left:850px;top:4375px">Hours of Operation<br>Open Daily 10:00 - 10:00</p>
<ul class="abs social-list">
  <li class="social">Snapgrid</li>
  <li class="social">Friendbook</li>
  <li class="social">Chirpline</li>
</ul>

</body>
</html>
```